Flyer for annual KESTREL SUMMIT 2020

I would like a church event flyer designed. The event is called "KESTREL SUMMIT 2020". I am looking for a professional, yet catchy design that uses our brand colors and logo creatively while communicating key information of the event effectively.

1. The logo is attached in two color formats. The designer has the choice to use them as he/she want.

2. The location of the event is: Harlow Community Center, 239 Fennimore Street, Portland, ME 04117

3. Time and date of event. The designer can organize and format the date and time as he/she pleases.
Thursday December 31st @ 6:30PM
Friday January 1st @ 6:30PM
Saturday 2nd @ 6:30PM
Sunday 3rd @ 4:30PM

4. The topic of the event is "In Fire and On Fire". The designer is free to use this phrase as he/she pleases to create a good composition.

5. Speaker: Prophet Marcus Olunde (2 pictures of the speaker to choose from are attached)

6. Contact information: contact@brightmeadowfold.org - Telephone number: 207 583 2914

7. I would also like the following three words on the flyer. These words describe the focus of the event: FIRE, REVIVAL, PROPHETIC

Target Market(s)

Young adults

Font styles to use
Sans Serif

Requirements
Must have
• Logo, speaker's picture
Should not have
• cross image, church image

```html
<!DOCTYPE html>
<html lang="en">
<head>
<meta charset="utf-8">
<title>Kestrel Summit 2020 – Flyer</title>
<link rel="stylesheet" href="https://fonts.googleapis.com/css2?family=Anton&family=Montserrat:wght@500;700;800;900&display=swap">
<style>
  :root {
    --night: #0b1a4a;
    --night-deep: #050d2c;
    --night-glow: #1f3c8f;
    --white: #ffffff;
    --gold: #f6c516;
    --fire-red: #d3161b;
    --ember: #e85a12;
    --flame: #f7a21b;
    --logo-blue: #123070;
    --suit-red: #8e1a22;
  }
  * { margin: 0; padding: 0; box-sizing: border-box; }
  html, body { width: 796px; height: 1200px; overflow: hidden; background: var(--night-deep); }
  body { font-family: "Montserrat", Arial, sans-serif; color: var(--white); }

  .flyer {
    position: relative;
    width: 796px;
    height: 1200px;
    overflow: hidden;
    background: radial-gradient(ellipse at 50% 30%, var(--night-glow) 0%, var(--night) 45%, var(--night-deep) 100%);
  }

  .event-title {
    position: absolute; top: 22px; left: 0; width: 100%;
    text-align: center;
  }
  .event-title__name {
    display: block;
    font-weight: 900; font-size: 88px; line-height: 1;
    letter-spacing: 2px;
  }
  .event-title__kind {
    display: block; margin-top: 4px;
    font-weight: 700; font-size: 30px; line-height: 1.1; letter-spacing: 12px;
  }
  .event-title__year {
    display: flex; align-items: center; justify-content: center; gap: 18px;
    margin-top: 2px;
    font-weight: 800; font-size: 30px; line-height: 1.1; letter-spacing: 3px;
  }
  .event-title__year::before, .event-title__year::after {
    content: ""; width: 70px; height: 3px; background: var(--white);
  }

  .speaker-photo {
    position: absolute; left: 40px; top: 220px; width: 340px; height: 680px;
    background: linear-gradient(180deg, #2a2f4a 0%, #5a2a30 35%, var(--suit-red) 70%, #5c1118 100%);
    border-radius: 150px 150px 0 0;
  }

  .speaker-label {
    position: absolute; left: 418px; top: 238px; width: 370px;
    color: var(--gold); font-weight: 800; font-size: 19px; line-height: 1.2;
    text-align: center; white-space: nowrap;
  }

  .venue {
    position: absolute; left: 418px; top: 276px; width: 370px;
    text-align: center; font-weight: 700; font-size: 12px; line-height: 1.4;
    text-transform: uppercase;
  }

  .schedule {
    position: absolute; left: 438px; top: 336px; width: 330px;
    border-collapse: collapse; font-size: 11px; font-weight: 700;
    text-transform: uppercase;
  }
  .schedule th, .schedule td {
    border: 1.5px solid var(--white); padding: 3px 6px; text-align: center;
  }
  .schedule th { font-weight: 800; }

  .bands { position: absolute; left: 0; top: 0; }

  .flames {
    position: absolute; left: 0; top: 0; width: 796px; height: 1200px;
    clip-path: polygon(0 1010px, 796px 800px, 796px 1200px, 0 1200px);
    background: linear-gradient(175deg, var(--flame) 0%, var(--ember) 40%, var(--fire-red) 75%, #6a0b0b 100%);
  }

  .theme-slogan {
    position: absolute; left: 398px; top: 829px;
    transform: translate(-50%, -50%) rotate(-14.6deg);
    font-family: "Anton", Impact, sans-serif; font-size: 66px; line-height: 1;
    font-weight: 400;
    color: var(--fire-red); white-space: nowrap; letter-spacing: 1px;
  }

  .focus-badge {
    position: absolute; left: 562px; top: 826px; width: 206px; height: 100px;
    transform: rotate(-12deg);
    background: var(--gold); border: 4px solid var(--fire-red); border-radius: 22px;
    display: flex; flex-direction: column; align-items: center; justify-content: center;
    color: var(--fire-red); font-weight: 900; font-size: 25px; line-height: 1.15;
  }

  .brand-mark {
    position: absolute; left: 262px; top: 1058px; width: 112px; height: 112px;
    background: var(--logo-blue);
    display: flex; align-items: center; justify-content: center;
    font-weight: 800; font-size: 24px; letter-spacing: 1px; color: var(--white);
  }

  .contact {
    position: absolute; right: 26px; top: 1096px;
    text-align: right; font-style: normal; font-weight: 500; font-size: 22px; line-height: 1.35;
  }
</style>
</head>
<body>
<main class="flyer">
  <header class="event-title">
    <span class="event-title__name">KESTREL</span>
    <span class="event-title__kind">SUMMIT</span>
    <span class="event-title__year">2020</span>
  </header>

  <div class="speaker-photo" role="img" aria-label="Portrait of Prophet Marcus Olunde in a red suit jacket"></div>

  <p class="speaker-label">Speaker: Prophet Marcus Olunde</p>

  <p class="venue">Location of the event:<br>Harlow Community Center,<br>239 Fennimore Street, Portland, ME 04117</p>

  <table class="schedule">
    <thead>
      <tr><th>Date</th><th>Hours</th></tr>
    </thead>
    <tbody>
      <tr><td>Thursday, December 31, 2020</td><td>6:30 P.M.</td></tr>
      <tr><td>Friday, January 1st, 2021</td><td>6:30 P.M.</td></tr>
      <tr><td>Saturday, January 2nd, 2021</td><td>6:30 P.M.</td></tr>
      <tr><td>Sunday, January 3rd, 2021</td><td>4:30 P.M.</td></tr>
    </tbody>
  </table>

  <div class="flames" role="img" aria-label="Blazing fire filling the lower part of the flyer"></div>

  <svg class="bands" width="796" height="1200" viewBox="0 0 796 1200" aria-hidden="true">
    <polygon points="0,856 796,648 796,662 0,870" fill="var(--gold)"/>
    <polygon points="0,870 796,662 796,680 0,888" fill="var(--fire-red)"/>
    <polygon points="0,888 796,680 796,770 0,978" fill="var(--white)"/>
    <polygon points="0,978 796,770 796,800 0,1010" fill="var(--fire-red)"/>
  </svg>

  <h2 class="theme-slogan">IN FIRE AND ON FIRE</h2>

  <div class="focus-badge">
    <span>FIRE</span>
    <span>REVIVAL</span>
    <span>PROPHETIC</span>
  </div>

  <div class="brand-mark">ARDEN</div>

  <address class="contact">
    Contact information:<br>
    contact@brightmeadowfold.org<br>
    Telephone number: 207 583 2914
  </address>
</main>
</body>
</html>
```